Pine Arbor Table & Chair Rentals

We need a business card for a table and chair rental company. We rent tables and chairs for weddings, funerals, business events and parties. We want something that looks clean and elegant while not being too busy. We would like colors in the green and blue hues and avoiding anything orange. We want to make sure the font is large enough to be seen easily.

Target Market(s)

Wedding & Event Rentals

Industry/Entity Type

Events

Contact Information for Business Card

Pine Arbor, sales@pinearborrentals.example, pinearborrentals.example, 555-218-0937

Requirements
Must have
• Easy to read font
Should not have
• Orange anywhere in the design

```html
<!DOCTYPE html>
<html lang="en">
<head>
<meta charset="utf-8">
<title>Pine Arbor Table &amp; Chair Rentals – Business Card</title>
<link rel="stylesheet" href="https://fonts.googleapis.com/css2?family=Open+Sans:wght@400;600&display=swap">
<style>
  :root {
    --backdrop: #3a3a3c;
    --card: #ffffff;
    --ink: #2e2a1f;
    --bark: #3a3527;
    --leaf: #5f7f12;
    --on-dark: #f4f2ea;
  }
  html, body {
    margin: 0;
    width: 1200px;
    height: 852px;
    overflow: hidden;
    background: var(--backdrop);
    font-family: "Open Sans", Arial, sans-serif;
  }
  .card {
    position: absolute;
    width: 525px;
    height: 300px;
    background: var(--card);
    border-radius: 22px;
    overflow: hidden;
    box-shadow: 0 10px 28px rgba(0,0,0,.35);
  }
  .card--front { left: 120px; top: 100px; }
  .card--back  { left: 555px; top: 452px; }

  .brand-name {
    margin: 0;
    color: var(--ink);
    font-weight: 400;
    font-size: 54px;
    line-height: 1;
    letter-spacing: 0.5px;
  }
  .front-lockup {
    position: absolute;
    left: 0; right: 0; top: 98px;
    text-align: center;
  }
  .tagline {
    margin: 14px 0 0;
    color: var(--ink);
    font-size: 24px;
    letter-spacing: 0.3px;
  }
  .back-lockup {
    position: absolute;
    left: 0; right: 0; top: 62px;
    text-align: center;
  }
  .bands { position: absolute; inset: 0; width: 100%; height: 100%; }
  .web {
    position: absolute;
    right: 18px; top: 266px;
    color: var(--on-dark);
    font-size: 14px;
    line-height: 1;
  }
  .contacts {
    position: absolute;
    left: 22px; bottom: 16px;
    margin: 0; padding: 0;
    list-style: none;
    color: var(--on-dark);
    font-size: 16px;
    line-height: 1.6;
  }
  .contacts li { display: flex; align-items: center; gap: 10px; }
  .contacts svg { width: 15px; height: 15px; fill: var(--on-dark); flex: none; }
</style>
</head>
<body>

<section class="card card--front" aria-label="Card front">
  <div class="front-lockup">
    <h1 class="brand-name">Pine Arbor</h1>
    <p class="tagline">Table and Chair Rentals</p>
  </div>
</section>

<section class="card card--back" aria-label="Card back">
  <svg class="bands" viewBox="0 0 525 300" preserveAspectRatio="none" aria-hidden="true">
    <polygon points="0,200 275,200 318,300 0,300" fill="var(--bark)"/>
    <polygon points="297,252 525,252 525,300 318,300" fill="var(--leaf)"/>
  </svg>
  <div class="back-lockup">
    <h2 class="brand-name">Pine Arbor</h2>
  </div>
  <div class="web">www.pinearborrentals.example</div>
  <ul class="contacts">
    <li>
      <svg viewBox="0 0 24 24" aria-hidden="true"><path d="M6.6 10.8a15.1 15.1 0 0 0 6.6 6.6l2.2-2.2a1 1 0 0 1 1-.25 11.4 11.4 0 0 0 3.6.57 1 1 0 0 1 1 1V20a1 1 0 0 1-1 1A17 17 0 0 1 3 4a1 1 0 0 1 1-1h3.5a1 1 0 0 1 1 1c0 1.25.2 2.45.57 3.57a1 1 0 0 1-.25 1z"/></svg>
      555-218-0937
    </li>
    <li>
      <svg viewBox="0 0 24 24" aria-hidden="true"><path d="M2 5h20v14H2z M3.5 6.5 12 13l8.5-6.5" fill="none" stroke="#f4f2ea" stroke-width="2"/></svg>
      sales@pinearborrentals.example
    </li>
  </ul>
</section>

</body>
</html>
```